Business Card Design Project

We require a business card template to cover basic contact information - our company logo, names of employees, title, mobile and email.
Updates

Target Market(s)

Corporate

Industry/Entity Type

Business

Font styles to use
Sans Serif

Requirements
Nice to have
• Thinking it would be great just to have the logo taking up approximately half the space (so it goes as far across the top of the card as possible) and then contact details in the lower half of the card. Keen just to use only the two colours in the logo, on a white background.
Should not have
• No fussy drawings

```html
<!DOCTYPE html>
<html lang="en">
<head>
<meta charset="utf-8">
<title>Tidewell Developments – Business Card</title>
<link rel="stylesheet" href="https://fonts.googleapis.com/css2?family=Arimo:wght@400&display=swap">
<style>
  :root {
    --brand-teal: #33a4b6;
    --brand-blue: #2d5fa6;
    --card-white: #ffffff;
    --backdrop: #ececec;
    --text-font: "Arimo", Arial, sans-serif;
  }
  html, body {
    margin: 0;
    padding: 0;
    width: 1200px;
    height: 900px;
    overflow: hidden;
    background: var(--backdrop);
  }
  .business-card {
    position: absolute;
    left: 100px;
    top: 165px;
    width: 1000px;
    height: 570px;
    background: var(--card-white);
    font-family: var(--text-font);
    box-shadow: 0 2px 6px rgba(0,0,0,0.12);
    overflow: hidden;
  }
  .company-name {
    position: absolute;
    left: 0;
    right: 0;
    top: 70px;
    margin: 0;
    text-align: center;
    font-size: 96px;
    font-weight: 400;
    letter-spacing: -1px;
    color: var(--brand-teal);
  }
  .employee {
    position: absolute;
    left: 0;
    right: 0;
    top: 255px;
    text-align: center;
    color: var(--brand-blue);
  }
  .employee-name {
    margin: 0;
    font-size: 44px;
    font-weight: 400;
  }
  .employee-title {
    margin: 4px 0 0;
    font-size: 28px;
  }
  .contact-band {
    position: absolute;
    left: 0;
    right: 0;
    bottom: 0;
    height: 165px;
    background: var(--brand-teal);
    color: var(--card-white);
    font-size: 28px;
  }
  .contact-phone {
    position: absolute;
    left: 60px;
    bottom: 30px;
    margin: 0;
    line-height: 1.3;
  }
  .contact-divider {
    position: absolute;
    left: 499px;
    top: 60px;
    width: 2px;
    height: 44px;
    background: var(--card-white);
  }
  .contact-email {
    position: absolute;
    right: 60px;
    top: 28px;
    margin: 0;
  }
</style>
</head>
<body>
  <article class="business-card">
    <h1 class="company-name">Tidewell Developments</h1>

    <div class="employee">
      <p class="employee-name">(Names of Employees)</p>
      <p class="employee-title">title</p>
    </div>

    <footer class="contact-band">
      <p class="contact-phone">Mobil Number<br>Fax</p>
      <span class="contact-divider" aria-hidden="true"></span>
      <p class="contact-email">Email address</p>
    </footer>
  </article>
</body>
</html>
```